Plakat-Design-Konrad-Wiesler
Zielgruppe
Wir sind eine Produktionsfirma für Musicals. Zielgruppe sind Musical Besucher (70% Weiblich)
Aufgabenstellung
Wir benötigen ein Plakat für ein Professionelles Musical.
Daten später bitte in InDesign und so groß als möglich.
Was soll aufs Plakat:
Name des Musicals: N`STÜCKCHEN HIMMEL
Das Musical von Konrad Wiesler
Untertittel: Swing`n Jive Winter
Texte: Horst Waldecker & Tobias Rehfeld
Buch: Gerald Pomsitz
Musik: Konrad Wiesler
Was soll das Plakat Vermitteln:
Die Story handelt von einem Musiker der aus der DDR geflohen ist in die BRD. Der Musiker lebt nun in Brighton (UK). Mit allen Facetten was dazu gehört, Stasi, Mauerschützen, Liebe, Verzweiflung...... Oder einfach gesagt: Ein Tolles Musical mit genialer Musik von Konrad Wiesler! „Keine Schlager Party“!! Sondern Seriös und einzigartig.
Eine Idee von mir ist eine Brücke bauen. Eventuell eine Gitarre als Brücke als Haupt Logo und obendrüber den Tittel. Oder eine Brücke mit Hammer und Sichel.
WOWW: Ich weiß die Angaben sind nicht wirklich Aussagekräftig, aber ich verlasse mich auf euer Künstlerisches Geschick.
Oben soll hin (über den Titel) Lutz Obermann Bühnenservice Global präsentiert:
Bitte nicht Kitschig. Eher Modern und klar.

```html
<!DOCTYPE html>
<html lang="de">
<head>
<meta charset="utf-8">
<title>N`STÜCKCHEN HIMMEL – Musical-Plakat</title>
<link rel="stylesheet" href="https://fonts.googleapis.com/css2?family=Montserrat:wght@200;700;800&display=swap">
<style>
  :root {
    --gold: #edd06c;
    --ink: #1f1f1f;
    --bar: #000000;
    --paper: #ffffff;
    --photo-light: #9a9a9a;
    --photo-dark: #1c1c1c;
  }
  * { margin: 0; padding: 0; box-sizing: border-box; }
  html, body { width: 848px; height: 1200px; overflow: hidden; background: var(--paper); }
  .poster {
    position: relative;
    width: 848px;
    height: 1200px;
    overflow: hidden;
    background: var(--paper);
    font-family: "Montserrat", sans-serif;
    color: var(--ink);
  }
  .dot { position: absolute; border-radius: 50%; }
  .dot--fill { background: var(--gold); }
  .dot--ring { border: 2px solid var(--gold); }
  .dot--hero { left: -230px; top: 75px; width: 732px; height: 732px; }
  .dot--top-right { left: 496px; top: -137px; width: 444px; height: 444px; }
  .dot--right { left: 717px; top: 551px; width: 168px; height: 168px; }
  .dot--accent { left: 342px; top: 858px; width: 44px; height: 44px; z-index: 0; }
  .dot--ring-title { left: 468px; top: 84px; width: 48px; height: 48px; }
  .dot--ring-right { left: 681px; top: 345px; width: 48px; height: 48px; }
  .dot--ring-low { left: 680px; top: 793px; width: 48px; height: 48px; }
  .dot--ring-edge { left: -24px; top: 824px; width: 48px; height: 48px; }

  .portrait {
    position: absolute;
    left: 153px; top: 223px;
    width: 594px; height: 594px;
    border-radius: 50%;
    background: radial-gradient(circle at 60% 40%, var(--photo-light) 0%, #5e5e5e 45%, var(--photo-dark) 100%);
  }

  .presenter {
    position: absolute;
    left: 52px; top: 40px;
    font-weight: 700;
    font-size: 13px;
    letter-spacing: 0.14em;
    color: var(--ink);
    white-space: nowrap;
  }

  .title {
    position: absolute;
    left: 50px; top: 78px;
    font-weight: 800;
    font-size: 46px;
    line-height: 64px;
    letter-spacing: 0.1em;
    color: var(--ink);
    white-space: nowrap;
  }
  .bar { position: absolute; background: var(--bar); }
  .bar--title { left: 69px; top: 223px; width: 191px; height: 16px; }
  .bar--credits { left: 430px; top: 1011px; width: 383px; height: 13px; }

  .composer {
    position: absolute;
    left: 52px; top: 822px;
    font-weight: 200;
    font-size: 46px;
    letter-spacing: 0.22em;
    color: var(--ink);
    white-space: nowrap;
    z-index: 1;
  }

  .tagline {
    position: absolute;
    left: 221px; top: 939px;
    font-weight: 700;
    font-size: 16px;
    line-height: 24px;
    letter-spacing: 0.12em;
    white-space: nowrap;
  }
  .tagline span, .credits span { display: block; }
  .credits {
    position: absolute;
    right: 70px; top: 1042px;
    text-align: right;
    font-weight: 700;
    font-size: 17px;
    line-height: 27px;
    letter-spacing: 0.14em;
    white-space: nowrap;
  }
</style>
</head>
<body>
<main class="poster">
  <div class="dot dot--fill dot--hero"></div>
  <div class="dot dot--fill dot--top-right"></div>
  <div class="dot dot--fill dot--right"></div>
  <div class="dot dot--ring dot--ring-title"></div>
  <div class="dot dot--ring dot--ring-right"></div>
  <div class="dot dot--ring dot--ring-low"></div>
  <div class="dot dot--ring dot--ring-edge"></div>

  <div class="portrait" role="img" aria-label="Schwarz-Weiß-Porträt des Komponisten Konrad Wiesler im dunklen Sakko vor einer Holztür"></div>

  <p class="presenter">LUTZ OBERMANN BÜHNENSERVICE GLOBAL PRÄSENTIERT:</p>
  <h1 class="title">N`STÜCKCHEN<br>HIMMEL</h1>
  <div class="bar bar--title"></div>

  <div class="dot dot--fill dot--accent"></div>
  <p class="composer">KONRAD WIESLER</p>

  <p class="tagline">
    <span>DAS MUSICAL VON KONRAD WIESLER</span>
    <span>UNTERTITTEL: SWING`N JIVE WINTER</span>
  </p>
  <div class="bar bar--credits"></div>

  <p class="credits">
    <span>TEXTE: HORST WALDECKER</span>
    <span>&amp; TOBIAS REHFELD</span>
    <span>BUCH: GERALD POMSITZ</span>
    <span>MUSIK: KONRAD WIESLER</span>
  </p>
</main>
</body>
</html>
```